Stationary for Beauty and Spa School

Create a business card, letterhead and envelopes (primarily #10 envelope with and without window and catalog envelope) for a beauty and wellness school in Miami, Fl. We offer 8 different programs of study and need an eye catching look. Looking for a combination of modern yet sophisticated. Nothing corporate or business looking. Would like to have a look and feel that is similar (or incorporates aspects) of a new website we will be launching in the next 30 days (screen shot attached.)

The final design should communicate style and elegance in a down to earth and friendly way. We strive to provide our students with quality education, friendly and amicable staff and experienced instructors.
Updates

Hello. FYI, in order to print an aesthetically appealing business card, we would like to print them (the business cards) using silk printing method, with spot UV coating (on some elements, maybe the logo, or depending on the design) and die cuts. Please think of this when preparing your design.

Only 1 day left, please submit your designs for selection. Thanks

Target Market(s)

Adults 18-49 years who are mostly interested in beauty and fashion. Need a youthful & modern look, yet sophisticated and elegant.

Industry/Entity Type

School

Colors
e34197
6b449b
add136
f79021

Requirements
Must have
• Similar look and feel as website (see attached screen shot)
Same look and feel of website (see attached screenshot)
Logo
Address: 5126 NW 14th Avenue. Miami, Fl 33157
Telephone: 305-914-3062
Fax: 786-552-4190
website/url: www.lumaroveacademy.edu
incorporate Photo of blonde model (attached)
Nice to have
• Tag line: "Beautify your future." Also, maybe two-sided business card. Would be nice if we could mention our programs (maybe in the back of the card). Below are the program offerings (names cannot be changed but order is irrelevant)... Cosmetology, Barber, Spa Therapy, Massage Therapy, Makeup Artistry, Skin Care, Manicure, Pedicure & Nail Extensions, Full Specialist.

A design with text plus a beautiful photo of a model is appealing. Attached to the files is a sample of a cover for a student handbook we have created. You should use the photo of the blonde model (attached) in your design. The original (quality) version of this stock photograph has been uploaded.

Also would be nice to request clients to follow us on facebook and instagram by including the icons.
Should not have
• A corporate or business look. We are a vocational school teaching beauty and spa programs and we like our advertising to have a look that resembles the industry. We do not want a very serious look or snobby feel.

```html
<!DOCTYPE html>
<html lang="en">
<head>
<meta charset="utf-8">
<title>Lumarove Academy – Business Cards</title>
<link rel="stylesheet" href="https://fonts.googleapis.com/css2?family=Arimo:wght@400;700&family=Open+Sans:wght@600&display=swap">
<style>
  :root {
    --backdrop: #262626;
    --lime: #afc43a;
    --violet: #5c0a9f;
    --orchid: #c41fcc;
    --amber: #e8b531;
    --ink: #2b2b2b;
    --paper: #ffffff;
    --muted: #3a3a3a;
    --social: #5aa2dc;
  }
  * { margin: 0; padding: 0; box-sizing: border-box; }
  html, body { width: 1200px; height: 615px; overflow: hidden; background: var(--backdrop); }
  .canvas { position: relative; width: 1200px; height: 615px; }

  .card { position: absolute; width: 357px; height: 197px; }
  .card--lime   { left: 45px;  top: 93px;  background: var(--lime); }
  .card--violet { left: 425px; top: 91px;  background: var(--violet); }
  .card--orchid { left: 45px;  top: 315px; background: var(--orchid); }
  .card--amber  { left: 425px; top: 314px; background: var(--amber); }

  .card__brand {
    position: absolute; left: 0; right: 0; top: 88px;
    text-align: center;
    font-family: "Open Sans", sans-serif; font-weight: 600;
    font-size: 25px; letter-spacing: 1px; color: var(--ink);
  }
  .card--violet .card__brand { color: var(--paper); }

  .card__tagline {
    position: absolute; left: 0; right: 0; top: 154px;
    text-align: center;
    font-family: "Arimo", sans-serif; font-size: 13.5px;
  }
  .card__tagline span {
    -webkit-background-clip: text; background-clip: text; color: transparent;
  }
  .card--lime .card__tagline span   { background-image: linear-gradient(90deg, var(--violet), var(--orchid)); }
  .card--violet .card__tagline span { background-image: linear-gradient(90deg, #c9a43a, var(--orchid)); }
  .card--orchid .card__tagline span { background-image: linear-gradient(90deg, var(--amber), #e2a84a); }
  .card--amber .card__tagline span  { background-image: linear-gradient(90deg, var(--violet), var(--orchid)); }

  .card--contact { left: 801px; top: 204px; background: var(--paper); font-family: "Arimo", sans-serif; color: var(--muted); }
  .card__stripe { position: absolute; left: 0; top: 0; width: 100%; height: 4px; display: flex; }
  .card__stripe i { flex: 1; }
  .card__stripe i:nth-child(1) { background: var(--lime); }
  .card__stripe i:nth-child(2) { background: var(--violet); }
  .card__stripe i:nth-child(3) { background: var(--orchid); }
  .card__stripe i:nth-child(4) { background: var(--amber); }

  .contact__brand {
    position: absolute; left: 16px; top: 47px;
    font-family: "Open Sans", sans-serif; font-weight: 600;
    font-size: 15px; letter-spacing: .5px; color: var(--ink);
  }
  .contact__name { position: absolute; left: 190px; top: 31px; font-size: 16.5px; color: var(--ink); }
  .contact__role { position: absolute; left: 190px; top: 52px; font-size: 10.5px; }
  .contact__rule { position: absolute; left: 190px; top: 93px; width: 153px; height: 1px; background: var(--violet); }
  .contact__lines { position: absolute; left: 190px; top: 104px; font-size: 10px; line-height: 13px; }
  .contact__lines p + p { margin-top: 0; }
  .contact__address { margin-top: 6px; }
  .contact__web { position: absolute; left: 190px; top: 167px; font-size: 10px; font-weight: 700; color: var(--ink); }

  .contact__social { position: absolute; left: 21px; top: 166px; display: flex; align-items: center; gap: 8px; font-size: 10px; }
  .contact__dot { width: 13px; height: 13px; border-radius: 50%; background: var(--social); }
</style>
</head>
<body>
<main class="canvas">
  <section class="card card--lime">
    <p class="card__brand">LUMAROVE ACADEMY</p>
    <p class="card__tagline"><span>BEAUTIFY YOUR FUTURE.</span></p>
  </section>
  <section class="card card--violet">
    <p class="card__brand">LUMAROVE ACADEMY</p>
    <p class="card__tagline"><span>BEAUTIFY YOUR FUTURE.</span></p>
  </section>
  <section class="card card--orchid">
    <p class="card__brand">LUMAROVE ACADEMY</p>
    <p class="card__tagline"><span>BEAUTIFY YOUR FUTURE.</span></p>
  </section>
  <section class="card card--amber">
    <p class="card__brand">LUMAROVE ACADEMY</p>
    <p class="card__tagline"><span>BEAUTIFY YOUR FUTURE.</span></p>
  </section>

  <section class="card card--contact">
    <div class="card__stripe"><i></i><i></i><i></i><i></i></div>
    <p class="contact__brand">LUMAROVE ACADEMY</p>
    <p class="contact__name">MARISOL VANCE</p>
    <p class="contact__role">Director</p>
    <div class="contact__rule"></div>
    <div class="contact__lines">
      <p>T&nbsp;&nbsp;&nbsp;305-914-3062</p>
      <p>F&nbsp;&nbsp;&nbsp;786-552-4190</p>
      <p class="contact__address">5126 NW 14th Avenue. Miami,<br>Fl 33157</p>
    </div>
    <p class="contact__web">www.lumaroveacademy.edu</p>
    <div class="contact__social"><span class="contact__dot"></span><span>/lumaroveacademy</span></div>
  </section>
</main>
</body>
</html>
```